Kestrel Bridge Consulting (KBC) Business Card Design

I would like to create double-sided business cards that contain:
1) Name: Derek Molvane
2) Phone Number: +1 (555) 218-4907
3) Email: Derek.Molvane@KestrelBridgeConsulting.example
4) Website: KestrelBridgeConsulting.example

I would like to include my logo and a color scheme similar to the Varnholt Grand Prix Ostera squad color scheme (black, silver, greenish-blue – but can also include regular blue)

What we do: Our company develops and delivers innovative and pragmatic information technology and cybersecurity risk and compliance solutions for organizations in the commercial market as well as the federal, and state/local sectors.

```html
<!DOCTYPE html>
<html lang="en">
<head>
<meta charset="utf-8">
<title>Kestrel Bridge Consulting – Business Card</title>
<link rel="stylesheet" href="https://fonts.googleapis.com/css2?family=Montserrat:wght@400;500;600;700&display=swap">
<style>
  :root {
    --stage: #2b2b2e;
    --card: #41429a;
    --card-pattern: #4a4ba6;
    --teal: #19c4c0;
    --white: #ffffff;
    --name-tone: #b4b6dc;
    --rule: rgba(255, 255, 255, 0.85);
  }
  * { box-sizing: border-box; margin: 0; padding: 0; }
  html, body {
    width: 1200px; height: 875px; overflow: hidden;
    background: var(--stage);
    font-family: "Montserrat", sans-serif;
    color: var(--white);
  }
  .sheet {
    width: 1200px; height: 875px;
    display: flex; flex-direction: column;
    align-items: center; justify-content: center; gap: 30px;
  }
  .card {
    position: relative;
    width: 680px; height: 388px;
    border-radius: 26px;
    background: var(--card);
    overflow: hidden;
  }

  /* Back side */
  .card-back .pattern-area {
    position: absolute; inset: 0;
    background: linear-gradient(135deg, var(--card-pattern), var(--card) 60%, var(--card-pattern));
  }
  .card-back .brand {
    position: absolute; left: 250px; top: 150px;
  }

  /* Brand lockup */
  .brand { display: flex; align-items: center; gap: 18px; }
  .brand-dot {
    width: 62px; height: 62px; border-radius: 50%;
    background: var(--teal); flex: none;
  }
  .brand-name {
    font-weight: 600; font-size: 22px; line-height: 1.08;
    letter-spacing: 0.12em; text-transform: uppercase;
    color: var(--white);
  }

  /* Front side */
  .card-front .brand { position: absolute; left: 60px; top: 52px; gap: 22px; }
  .card-front .brand-dot { width: 88px; height: 88px; }
  .card-front .brand-name { font-size: 30px; }
  .top-rule {
    position: absolute; left: 330px; right: 40px; top: 168px;
    height: 1.5px; background: var(--rule);
  }
  .person { position: absolute; left: 60px; top: 210px; }
  .person-name {
    font-weight: 700; font-size: 32px; color: var(--name-tone);
    letter-spacing: 0.01em;
  }
  .person-title {
    font-weight: 500; font-size: 15px; letter-spacing: 0.06em;
    text-transform: uppercase; margin-top: 2px;
  }
  .person-rule {
    width: 250px; height: 1.5px; background: var(--rule); margin: 14px 0 12px;
  }
  .contact-list { list-style: none; }
  .contact-item {
    display: flex; align-items: center; gap: 12px;
    font-size: 15px; font-weight: 400; line-height: 1.75;
  }
  .contact-icon { width: 15px; height: 15px; flex: none; }
</style>
</head>
<body>
<main class="sheet">

  <section class="card card-back" aria-label="Card back">
    <div class="pattern-area" role="img" aria-label="Faint repeating brand emblem pattern in tonal purple"></div>
    <div class="brand">
      <span class="brand-dot"></span>
      <span class="brand-name">Kestrel<br>Bridge<br>Consulting</span>
    </div>
  </section>

  <section class="card card-front" aria-label="Card front">
    <div class="brand">
      <span class="brand-dot"></span>
      <span class="brand-name">Kestrel<br>Bridge<br>Consulting</span>
    </div>
    <div class="top-rule"></div>

    <div class="person">
      <h1 class="person-name">Derek Molvane</h1>
      <p class="person-title">Managing Director</p>
      <div class="person-rule"></div>
      <ul class="contact-list">
        <li class="contact-item">
          <svg class="contact-icon" viewBox="0 0 24 24" fill="none" stroke="#fff" stroke-width="2" stroke-linecap="round" stroke-linejoin="round">
            <path d="M5 3h4l2 5-2.5 1.5a11 11 0 0 0 6 6L16 13l5 2v4a2 2 0 0 1-2 2A17 17 0 0 1 3 5a2 2 0 0 1 2-2z"/>
          </svg>
          <span>+1 (555) 218-4907</span>
        </li>
        <li class="contact-item">
          <svg class="contact-icon" viewBox="0 0 24 24" fill="none" stroke="#fff" stroke-width="2" stroke-linejoin="round">
            <rect x="2" y="5" width="20" height="14" rx="1"/>
            <path d="M2 6l10 7 10-7"/>
          </svg>
          <span>Derek.Molvane@KestrelBridgeConsulting.example</span>
        </li>
        <li class="contact-item">
          <svg class="contact-icon" viewBox="0 0 24 24" fill="none" stroke="#fff" stroke-width="2">
            <circle cx="12" cy="12" r="10"/>
            <ellipse cx="12" cy="12" rx="4" ry="10"/>
            <path d="M2 12h20M4 7h16M4 17h16"/>
          </svg>
          <span>KestrelBridgeConsulting.example</span>
        </li>
      </ul>
    </div>
  </section>

</main>
</body>
</html>
```